Boutique Film/TV Company needs Business Card Design

Please see our website for background on our company and look of our current logo: www.morlandpictures.ca

Pantone 314U is our main colour.

Target Market(s)

Network of peers, funders and broadcasters.

Industry/Entity Type

Business

Requirements
Must have
• We would like rounded corners and the height of the card to be shorter than traditional (maybe?!)

It's important that we have room for our office address, office number, cell number, email address, website, facebook and linked-in info (though not all of us have a linked-in account).

Would like the logo to keep the exclamation marks over the letters but the tag line/tag words of "film - television - interactive" can stay or go or... surprise me!

Nice to have
• Silky matte finish.

We are open to a change in the font of our logo/name.

```html
<!DOCTYPE html>
<html lang="en">
<head>
<meta charset="utf-8">
<title>Morland Pictures – Business Card</title>
<link rel="stylesheet" href="https://fonts.googleapis.com/css2?family=Ubuntu:wght@300;400;500;700&family=Arimo:wght@700&display=swap">
<style>
  :root {
    --brand-teal: #1b87a6;
    --brand-teal-dark: #146f89;
    --ink: #1d1d1d;
    --ink-soft: #3a3a3a;
    --card-white: #ffffff;
    --card-back: #f3f4f4;
    --backdrop: #e4e8ea;
  }
  * { box-sizing: border-box; margin: 0; padding: 0; }
  html, body { width: 1200px; height: 960px; overflow: hidden; }
  body {
    background: var(--backdrop);
    font-family: "Ubuntu", Arial, sans-serif;
    color: var(--ink);
    position: relative;
  }
  .card {
    position: absolute;
    left: 280px;
    width: 640px;
    height: 340px;
    border-radius: 48px;
    overflow: hidden;
    box-shadow: 0 10px 28px rgba(0,0,0,.14);
  }
  /* Front */
  .card--front { top: 90px; background: var(--card-white); }
  .wordmark {
    position: absolute;
    font-family: "Ubuntu", Arial, sans-serif;
    font-weight: 400;
    letter-spacing: 0.5px;
    line-height: 1;
  }
  .card--front .wordmark { left: 56px; top: 44px; font-size: 66px; color: var(--brand-teal); }
  .name-tab {
    position: absolute; left: 0; top: 172px; width: 26px; height: 46px;
    background: var(--brand-teal);
  }
  .holder {
    position: absolute; left: 44px; top: 178px;
    font-size: 29px; font-weight: 400; color: var(--ink);
  }
  .holder__role { font-size: 22px; color: var(--ink-soft); }
  .web-band {
    position: absolute; left: 392px; right: 0; top: 140px; height: 44px;
    background: var(--brand-teal);
    color: var(--card-white);
    font-size: 16px; letter-spacing: 2px;
    display: flex; align-items: center; padding-left: 20px;
  }
  .office {
    position: absolute; left: 400px; top: 222px;
    font-size: 14px; line-height: 19px; color: var(--ink-soft);
  }
  .office__company { font-weight: 700; color: var(--ink); }
  .contact-list {
    position: absolute; left: 36px; top: 244px;
    list-style: none; font-size: 17px; line-height: 22px; color: var(--ink);
  }
  .contact-list li { display: flex; align-items: center; gap: 14px; }
  .contact-list svg { width: 13px; height: 13px; fill: var(--brand-teal); flex: none; }
  /* Back */
  .card--back { top: 510px; background: var(--card-back); }
  .back-band {
    position: absolute; left: 0; right: 0; top: 104px; height: 28px;
    background: var(--brand-teal);
  }
  .back-plate {
    position: absolute; left: 150px; top: 52px; width: 340px; height: 140px;
    border-radius: 12px;
    background: linear-gradient(135deg, var(--brand-teal-dark), var(--brand-teal) 60%, #3a9fbb);
    display: flex; flex-direction: column; align-items: center; justify-content: center; gap: 10px;
  }
  .back-plate .wordmark { position: static; font-size: 64px; color: var(--card-white); }
  .tagline {
    font-family: "Arimo", Arial, sans-serif; font-weight: 700;
    font-size: 15px; color: var(--card-white); letter-spacing: 0.3px;
  }
</style>
</head>
<body>

<section class="card card--front" aria-label="Business card front">
  <div class="wordmark">Morland</div>
  <div class="name-tab"></div>
  <p class="holder">Dana Whitlock <span class="holder__role">/ Manager</span></p>
  <div class="web-band">www.morlandpictures.ca</div>
  <address class="office" style="font-style:normal">
    <div class="office__company">Morland Pictures Inc.</div>
    <div>28 Alder Lane</div>
    <div>Toronto, ON, M4K 2P9</div>
  </address>
  <ul class="contact-list">
    <li><svg viewBox="0 0 16 16" aria-hidden="true"><path d="M3 1l3 3-1.5 2a9 9 0 0 0 5.5 5.5L12 10l3 3-2 2C7 15 1 9 1 3z"/></svg>416.555.0182</li>
    <li><svg viewBox="0 0 16 16" aria-hidden="true"><path d="M4 0h8a1 1 0 0 1 1 1v14a1 1 0 0 1-1 1H4a1 1 0 0 1-1-1V1a1 1 0 0 1 1-1zm1 2v8h6V2zm3 10a1.2 1.2 0 1 0 0 2.4A1.2 1.2 0 0 0 8 12z"/></svg>416.555.0147</li>
    <li><svg viewBox="0 0 16 16" aria-hidden="true"><path d="M1 6l7-5 7 5v9H1zm2 1.2V13h10V7.2L8 11z"/></svg>dana@morlandpictures.ca</li>
    <li><svg viewBox="0 0 16 16" aria-hidden="true"><rect x="1" y="1" width="14" height="14" rx="2"/></svg>/morlandpictures</li>
  </ul>
</section>

<section class="card card--back" aria-label="Business card back">
  <div class="back-band"></div>
  <div class="back-plate">
    <div class="wordmark">Morland</div>
    <div class="tagline">Films • Television • Interactive</div>
  </div>
</section>

</body>
</html>
```